Dutch psychology podcast needs logo / art design

I need a logo / artwork for my new podcast on psychology/health called 'Het Heldere Kwartier'. In the podcast I talk to different experts on subjects as personal development, psychology, health, spirituality and entrepreneurship. I would like to see my brand colors back in the design (www.joramveldkuijl.nl) and my face in the artwork since I'm the host of the show.

My photo is included in the attachments and I've also added some examples of what I'm looking for.

Industry/Entity Type

Psychology

Colors

Designer to choose colors to be used in the design.

Requirements
Must have
• - Name of the show: 'Het Heldere Kwartier' (I prefer that this name is turned into a logo), see attachment of example of Harbor of Wonder
• - Subtitle: 'met Joram Veldkuijl' which is my name a the host
• - My picture, see attachments

```html
<!DOCTYPE html>
<html lang="nl">
<head>
<meta charset="utf-8">
<title>Het Heldere Kwartier – podcast artwork</title>
<link rel="stylesheet" href="https://fonts.googleapis.com/css2?family=Montserrat:wght@800;900&display=swap">
<style>
  :root {
    --teal: #2aa5a0;
    --yellow: #fcdd68;
    --ink: #000000;
    --white: #ffffff;
    --coral: #ef6b72;
    --sweater: #1a1c2c;
    --skin: #c99a80;
  }
  html, body {
    margin: 0;
    padding: 0;
    width: 1200px;
    height: 1200px;
    overflow: hidden;
    background: var(--teal);
  }
  .cover {
    position: relative;
    width: 1200px;
    height: 1200px;
    background: var(--teal);
    overflow: hidden;
    font-family: "Montserrat", sans-serif;
  }
  .title-plate {
    position: absolute;
    left: 0;
    top: 0;
  }
  .show-title {
    position: absolute;
    left: 178px;
    top: 41px;
    margin: 0;
    font-weight: 900;
    font-size: 118px;
    line-height: 118px;
    letter-spacing: -2px;
    color: var(--ink);
    white-space: nowrap;
  }
  .show-title span { display: block; }
  .host-photo {
    position: absolute;
    left: 560px;
    top: 372px;
    width: 620px;
    height: 828px;
    border-radius: 300px 300px 0 0;
    background: linear-gradient(to bottom, #3a2e28 0%, var(--skin) 14%, var(--skin) 44%, var(--sweater) 56%, var(--sweater) 100%);
  }
  .met-badge {
    position: absolute;
    left: 357px;
    top: 748px;
    width: 184px;
    height: 184px;
    border-radius: 50%;
    background: var(--yellow);
    display: flex;
    align-items: center;
    justify-content: center;
    font-weight: 900;
    font-size: 58px;
    color: var(--ink);
    letter-spacing: -1px;
  }
  .host-name { margin: 0; }
  .host-name span {
    position: absolute;
    left: 449px;
    background: var(--ink);
    color: var(--white);
    font-weight: 800;
    font-size: 80px;
    line-height: 1;
    display: flex;
    align-items: center;
    padding-left: 30px;
    box-sizing: border-box;
    letter-spacing: 2px;
    white-space: nowrap;
  }
  .host-name .first {
    top: 958px;
    height: 110px;
    padding-right: 40px;
  }
  .host-name .last {
    top: 1089px;
    width: 751px;
    height: 111px;
  }
</style>
</head>
<body>
  <main class="cover">
    <svg class="title-plate" width="1200" height="1200" viewBox="0 0 1200 1200" aria-hidden="true">
      <path d="M30 33 H616 A196 196 0 0 1 616 425 H30 Z" fill="var(--yellow)" stroke="var(--ink)" stroke-width="4"/>
      <circle cx="116" cy="238" r="44" fill="var(--coral)"/>
    </svg>

    <h1 class="show-title">
      <span>Het</span>
      <span>Heldere</span>
      <span>Kwartier</span>
    </h1>

    <div class="host-photo" role="img" aria-label="Portretfoto van host Joram Veldkuijl, glimlachend, in donkere trui met armen over elkaar"></div>

    <div class="met-badge">met</div>

    <h2 class="host-name">
      <span class="first">JORAM</span>
      <span class="last">VELDKUIJL</span>
    </h2>
  </main>
</body>
</html>
```